Verin Subscription Infographic

I need an infographic to promote my new subscription service.
The infographic should be clear and consise, showcasing the benefits and the value of my offering.
I have provided a PDF that describes the service, and the offering in detail. I would like the designer to read the pdf document, understand the offering and design a one page infographic that will condense the information in a nice, visual way, to be shared within Brightlink for advertisment purposes.

```html
<!DOCTYPE html>
<html lang="en">
<head>
<meta charset="utf-8">
<title>Verin Subscription Plans</title>
<link href="https://fonts.googleapis.com/css2?family=Montserrat:wght@500;600;700&family=Noto+Serif:wght@400&display=swap" rel="stylesheet">
<style>
:root{
  --navy:#0d0f3d;
  --ink:#16183a;
  --teal:#80cfd9;
  --cell:#f2f5f8;
  --tag:#c9e7d5;
  --white:#ffffff;
}
*{box-sizing:border-box;margin:0;padding:0}
html,body{width:1200px;height:849px;overflow:hidden;background:var(--white)}
body{font-family:"Montserrat",sans-serif;color:var(--ink);position:relative}
.header{position:absolute;left:0;top:0;width:1200px;height:160px}
.header-photo{position:absolute;left:300px;top:0;width:900px;height:160px;
  background:linear-gradient(90deg,#ffffff 0%,#e9e4e2 18%,#9a8f8c 45%,#6b5f5c 55%,#b07a68 75%,#a6553d 100%)}
.brand{position:absolute;left:44px;top:46px;display:flex;align-items:center;gap:14px}
.brand-dot{width:60px;height:60px;border-radius:50%;background:var(--navy)}
.brand-name{font-weight:700;font-size:52px;color:var(--navy);letter-spacing:-1px}
.plans{position:absolute;left:26px;top:178px;width:1151px;height:648px;display:grid;
  grid-template-columns:191px repeat(5,1fr);
  grid-template-rows:53px 63px 54px 55px 55px 81px 1fr;gap:2px;background:var(--white)}
.plans > div{display:flex;align-items:center;justify-content:center;text-align:center}
.col-head{background:var(--navy);color:var(--white);font-size:21px;font-weight:500}
.row-label{background:var(--teal);font-size:18px;font-weight:500;line-height:1.3;color:var(--navy)}
.value{background:var(--cell);font-size:21px;font-weight:500}
.support{background:var(--cell);font-size:16px;font-weight:500;line-height:1.3}
.plans > .row-label.tools{align-items:flex-start;padding-top:22px}
.plans > .tools-cell{background:var(--cell);align-items:flex-start;justify-content:flex-start;flex-direction:column;text-align:left;padding:8px 6px}
.tag{display:inline-block;background:var(--tag);font-family:"Noto Serif",serif;font-size:14px;padding:1px 6px;margin:0 0 5px 1px;color:var(--navy);width:150px}
.tag.short{width:136px}
.tools-list{list-style:none;font-size:11px;line-height:1.25;margin:0 0 10px 8px;display:grid;grid-template-columns:1fr;column-gap:10px;width:170px}
.tools-list.two{grid-template-columns:auto auto}
.tools-list li::before{content:"• ";}
</style>
</head>
<body>
<header class="header">
  <div class="header-photo" role="img" aria-label="Close-up photograph of a copper-wound electric motor stator"></div>
  <div class="brand"><span class="brand-dot"></span><span class="brand-name">Verin</span></div>
</header>

<main class="plans">
  <div class="col-head">Subscription</div>
  <div class="col-head">Starter</div>
  <div class="col-head">Entry</div>
  <div class="col-head">Member</div>
  <div class="col-head">Premium</div>
  <div class="col-head">Exclusive</div>

  <div class="row-label">Full Time<br>Equivalent</div>
  <div class="value">1 FTE</div><div class="value">2 FTE</div><div class="value">3 FTE</div><div class="value">4 FTE</div><div class="value">5 FTE</div>

  <div class="row-label">Price (Monthly)</div>
  <div class="value">£9,280</div><div class="value">£17,120</div><div class="value">£24,900</div><div class="value">£32,000</div><div class="value">£39,600</div>

  <div class="row-label">Engineering<br>Hours Pool</div>
  <div class="value">160</div><div class="value">320</div><div class="value">480</div><div class="value">640</div><div class="value">800</div>

  <div class="row-label">Equivalent<br>Hourly Price</div>
  <div class="value">£58</div><div class="value">£53.5</div><div class="value">£51.9</div><div class="value">£50</div><div class="value">£49.5</div>

  <div class="row-label">OnSite Support</div>
  <div class="support">Online<br>Support only</div>
  <div class="support">1 Engineer<br>Semi-pernamenently<br>on Site</div>
  <div class="support">1 Engineer<br>Semi-pernamenently<br>on Site</div>
  <div class="support">1 Engineers on site<br>1 Engineer<br>Semi-permanently</div>
  <div class="support">1 Engineers on site<br>1 Engineer<br>Semi-permanently</div>

  <div class="row-label tools">Tools Access</div>
  <div class="tools-cell">
    <span class="tag short">Mainstream Tools</span>
    <ul class="tools-list"><li>Emails</li><li>Accounts</li><li>Deskwork Suite</li><li>Taskline</li></ul>
  </div>
  <div class="tools-cell">
    <span class="tag short">Mainstream Tools</span>
    <ul class="tools-list two"><li>Emails</li><li>Deskwork Suite</li><li>Accounts</li><li>Taskline</li></ul>
    <span class="tag">Engineering Tools</span>
    <ul class="tools-list"><li>Reliaform</li><li>Verin In house</li><li>Calculators</li></ul>
  </div>
  <div class="tools-cell">
    <span class="tag short">Mainstream Tools</span>
    <ul class="tools-list two"><li>Emails</li><li>Deskwork Suite</li><li>Accounts</li><li>Taskline</li></ul>
    <span class="tag">Engineering Tools</span>
    <ul class="tools-list"><li>Reliaform</li><li>Verin In house</li><li>Calculators</li></ul>
    <span class="tag">Specialist Tools</span>
    <ul class="tools-list"><li>Numerix Lab</li><li>Blockflow</li></ul>
  </div>
  <div class="tools-cell">
    <span class="tag short">Mainstream Tools</span>
    <ul class="tools-list two"><li>Emails</li><li>Deskwork Suite</li><li>Accounts</li><li>Taskline</li></ul>
    <span class="tag">Engineering Tools</span>
    <ul class="tools-list"><li>Reliaform</li><li>Verin In house</li><li>Calculators</li></ul>
    <span class="tag">Specialist Tools</span>
    <ul class="tools-list"><li>Numerix Lab</li><li>Blockflow</li></ul>
    <span class="tag">High end software</span>
    <ul class="tools-list two"><li>RotorDraft</li><li>Solvix (Mech)</li></ul>
  </div>
  <div class="tools-cell">
    <span class="tag short">Mainstream Tools</span>
    <ul class="tools-list two"><li>Emails</li><li>Deskwork Suite</li><li>Accounts</li><li>Taskline</li></ul>
    <span class="tag">Engineering Tools</span>
    <ul class="tools-list two"><li>Reliaform</li><li>Calculators</li><li>Verin In house</li></ul>
    <span class="tag">Specialist Tools</span>
    <ul class="tools-list two"><li>Numerix Lab</li><li>Blockflow</li></ul>
    <span class="tag">High end software</span>
    <ul class="tools-list two"><li>RotorDraft</li><li>Solvix (Mech)</li></ul>
    <span class="tag">Specialist Software</span>
    <ul class="tools-list two"><li>Geartrace</li><li>Linkwork MultiBody</li></ul>
  </div>
</main>
</body>
</html>
```